1 OZ TRANSDERMAL CBD. NOVEL, INNOVATIVE FIRST TIME EVER OF CBD THAT PENETRATES THROUGH SKIN.
BRAND: VELORA WELLNESS
NAME: CBD SURGE

Target Market(s)

CBD users waiting a smarter way-through the skin. None lost in toilet like other CBD, directly into you within 5 minutes.

Requirements
Must have
• Elegant, bold, natural, NOT THE SAME OLD CBD. Jump off shelf.
Should not have
• Boring "me-too" labels.

```html
<!DOCTYPE html>
<html lang="en">
<head>
<meta charset="utf-8">
<title>Velora Wellness – CBD Surge Labels</title>
<link rel="stylesheet" href="https://fonts.googleapis.com/css2?family=Montserrat:wght@700&family=Josefin+Sans:wght@400&display=swap">
<style>
  :root {
    --forest: #1c4535;
    --leaf: #3b6b4f;
    --ink: #000000;
    --paper: #ffffff;
    --paper-shade: #d9d9d9;
    --text-dark: #111111;
  }
  html, body {
    margin: 0;
    width: 1200px;
    height: 1000px;
    overflow: hidden;
    background: var(--paper);
  }
  .canvas { position: relative; width: 1200px; height: 1000px; }
  .label { position: absolute; display: block; }
  .label--green { left: 66px; top: 318px; width: 333px; height: 437px; }
  .label--black { left: 435px; top: 318px; width: 331px; height: 437px; }
  .label--wide  { left: 815px; top: 522px; width: 297px; height: 346px; }

  .band--green { fill: var(--forest); }
  .band--black { fill: var(--ink); }
  .rule--green { stroke: var(--forest); }
  .rule--black { stroke: var(--ink); }

  .brand-name {
    font-family: "Montserrat", sans-serif;
    font-weight: 700;
    text-anchor: middle;
  }
  .brand-name--green { fill: var(--leaf); }
  .brand-name--black { fill: var(--ink); }
  .est {
    font-family: "Montserrat", sans-serif;
    font-weight: 700;
    font-size: 11px;
    fill: var(--text-dark);
  }
  .tagline {
    font-family: "Josefin Sans", sans-serif;
    font-size: 9.5px;
    fill: var(--text-dark);
    text-anchor: middle;
  }
  .mark--green { fill: var(--leaf); }
  .mark--black { fill: var(--ink); }
</style>
</head>
<body>
<main class="canvas">

  <!-- Green label -->
  <svg class="label label--green" viewBox="0 0 333 437">
    <defs>
      <linearGradient id="paperGreen" x1="0" x2="1">
        <stop offset="0" stop-color="var(--paper)"/>
        <stop offset="0.55" stop-color="#f4f4f4"/>
        <stop offset="1" stop-color="var(--paper-shade)"/>
      </linearGradient>
    </defs>
    <rect width="333" height="437" fill="url(#paperGreen)"/>
    <polygon class="band--green" points="0,0 333,0 333,92 166,50 0,92"/>
    <polyline class="rule--green" fill="none" stroke-width="3" points="0,107 166,64 333,107"/>
    <polyline class="rule--green" fill="none" stroke-width="3" points="0,330 166,373 333,330"/>
    <polygon class="band--green" points="0,342 166,388 333,342 333,437 0,437"/>
    <circle class="mark--green" cx="166" cy="152" r="11"/>
    <text class="est" x="202" y="160">2020</text>
    <text class="brand-name brand-name--green" x="166" y="218" font-size="40" letter-spacing="12">SURGE</text>
    <text class="brand-name brand-name--green" x="168" y="257" font-size="30" letter-spacing="10">CBD</text>
    <line class="rule--green" x1="133" y1="276" x2="199" y2="276" stroke-width="2"/>
    <text class="tagline" x="166" y="306">CBD users waiting a smarter way-through the skin</text>
    <text class="tagline" x="166" y="320">None lost in toilet like other CBD, directly into you within</text>
    <text class="tagline" x="166" y="334">5 minutes</text>
  </svg>

  <!-- Black label -->
  <svg class="label label--black" viewBox="0 0 331 437">
    <rect width="331" height="437" fill="var(--paper)"/>
    <polygon class="band--black" points="0,0 331,0 331,92 165,50 0,92"/>
    <polyline class="rule--black" fill="none" stroke-width="3" points="0,107 165,64 331,107"/>
    <polyline class="rule--black" fill="none" stroke-width="3" points="0,330 165,373 331,330"/>
    <polygon class="band--black" points="0,342 165,388 331,342 331,437 0,437"/>
    <text class="est" x="100" y="158">EST</text>
    <circle class="mark--black" cx="165" cy="154" r="11"/>
    <text class="est" x="200" y="158">2020</text>
    <text class="brand-name brand-name--black" x="165" y="216" font-size="40" letter-spacing="12">SURGE</text>
    <text class="brand-name brand-name--black" x="167" y="255" font-size="30" letter-spacing="10">CBD</text>
    <line class="rule--black" x1="133" y1="274" x2="197" y2="274" stroke-width="2"/>
    <text class="tagline" x="165" y="306">CBD users waiting a smarter way-through the skin</text>
    <text class="tagline" x="165" y="320">None lost in toilet like other CBD, directly into you within</text>
    <text class="tagline" x="165" y="334">5 minutes</text>
  </svg>

  <!-- Wide green label -->
  <svg class="label label--wide" viewBox="0 0 297 346">
    <defs>
      <linearGradient id="paperWide" x1="0" x2="1">
        <stop offset="0" stop-color="var(--paper)"/>
        <stop offset="0.55" stop-color="#f4f4f4"/>
        <stop offset="1" stop-color="var(--paper-shade)"/>
      </linearGradient>
    </defs>
    <rect width="297" height="346" fill="url(#paperWide)"/>
    <polygon class="band--green" points="0,0 297,0 297,44 148,8 0,44"/>
    <polyline class="rule--green" fill="none" stroke-width="3" points="0,55 148,20 297,55"/>
    <polyline class="rule--green" fill="none" stroke-width="3" points="0,250 148,282 297,250"/>
    <polygon class="band--green" points="0,260 148,294 297,260 297,346 0,346"/>
    <text class="est" x="88" y="99">EST</text>
    <circle class="mark--green" cx="148" cy="95" r="10"/>
    <text class="est" x="180" y="99">2020</text>
    <text class="brand-name brand-name--green" x="148" y="150" font-size="34" letter-spacing="10">SURGE</text>
    <text class="brand-name brand-name--green" x="150" y="184" font-size="26" letter-spacing="9">CBD</text>
    <line class="rule--green" x1="116" y1="200" x2="176" y2="200" stroke-width="2"/>
    <text class="tagline" x="148" y="231" font-size="9">CBD users waiting a smarter way-through the skin</text>
    <text class="tagline" x="148" y="243" font-size="9">None lost in toilet like other CBD, directly into you within</text>
    <text class="tagline" x="148" y="255" font-size="9">5 minutes</text>
  </svg>

</main>
</body>
</html>
```